Infografik für unabhängigen Finanzdienstleister
Zielgruppe
Wir sind eine unabhängiger Finanzdienstleister mit dem Schwerpunkt der Kapitalanlage und dem Fokus auf vermögende Privatkunden. Wir sind nur unseren Mandanten verpflichtet, da diese unsere Dienstleistung transparent und frei von versteckten Provisionen honorieren.
Aufgabenstellung
Klassisch modern, aber nicht verspielt. Ein Gefühl gibt unsere Homepage. Weitere Infos zum Projekt habe ich hier in einem kurzen Video verfasst: https://lobark.vemiko-kanzlei.example/message?id=7f91c3a5e2d04b
Ergänzung:
Die Grafik soll sich mehr 'selbst erklären lassen' als sie es derzeit tut. Zudem soll die Prozessreihenfolge besser verdeutlicht werden...

```html
<!DOCTYPE html>
<html lang="de">
<head>
<meta charset="utf-8">
<title>Unser Beratungskonzept – VEMIKO</title>
<link rel="stylesheet" href="https://fonts.googleapis.com/css2?family=Montserrat:wght@600;700;800&family=Oswald:wght@400&display=swap">
<style>
  :root {
    --stage: #a9a9a9;
    --black: #000000;
    --gold: #9d7126;
    --gold-light: #b8975e;
    --cream: #f5ecd9;
    --white: #ffffff;
    --mist: #e2e6e7;
    --mist-top: #eef1f2;
    --sand: #f4f3f0;
    --navy: #2c3440;
    --slate: #4b5c6b;
    --ink: #2f3640;
  }
  html, body { margin: 0; padding: 0; overflow: hidden; }
  body { width: 1166px; height: 1200px; background: var(--stage); }
  .canvas { display: block; width: 1166px; height: 1200px; }
  .title { font-family: "Montserrat", sans-serif; font-weight: 800; fill: var(--gold); }
  .title-small { font-size: 45px; }
  .title-large { font-size: 57px; }
  .label-condensed { font-family: "Oswald", sans-serif; font-weight: 400; font-size: 18px; text-anchor: middle; }
  .label-cream { fill: var(--cream); }
  .label-ink { fill: var(--ink); }
  .label-white { fill: var(--white); }
  .audience { font-family: "Montserrat", sans-serif; font-weight: 700; font-size: 15.5px; fill: var(--white); text-anchor: middle; letter-spacing: 0.3px; }
  .offer { font-family: "Montserrat", sans-serif; font-weight: 700; font-size: 10.6px; fill: var(--white); text-anchor: middle; letter-spacing: 0.3px; }
  .step-number { font-family: "Montserrat", sans-serif; font-weight: 800; font-size: 27px; fill: var(--white); text-anchor: middle; }
  .step-title { font-family: "Montserrat", sans-serif; font-weight: 700; font-size: 12px; fill: var(--white); text-anchor: middle; }
  .step-item { font-family: "Montserrat", sans-serif; font-weight: 700; font-size: 8.2px; fill: var(--white); text-anchor: middle; letter-spacing: 0.1px; }
  .bullet { fill: var(--gold-light); }
  .footer-name { font-family: "Montserrat", sans-serif; font-weight: 700; font-size: 11.5px; fill: var(--white); text-anchor: middle; letter-spacing: 0.4px; }
</style>
</head>
<body>
<svg class="canvas" viewBox="0 0 1166 1200" xmlns="http://www.w3.org/2000/svg">
  <defs>
    <clipPath id="header-clip"><rect x="70" y="138" width="1032" height="228"/></clipPath>
    <radialGradient id="globe-tone" cx="50%" cy="50%" r="50%">
      <stop offset="0%" stop-color="#3e3e3e"/>
      <stop offset="70%" stop-color="#2a2a2a"/>
      <stop offset="100%" stop-color="#161616"/>
    </radialGradient>
    <radialGradient id="emblem-tone" cx="50%" cy="50%" r="50%">
      <stop offset="0%" stop-color="#f6f0e2"/>
      <stop offset="100%" stop-color="#d9c8a2"/>
    </radialGradient>
    <linearGradient id="people-tone" x1="0" y1="0" x2="0" y2="1">
      <stop offset="0%" stop-color="#e9ecee"/>
      <stop offset="100%" stop-color="#c4c8cc"/>
    </linearGradient>
    <linearGradient id="mist-fade" x1="0" y1="0" x2="0" y2="1">
      <stop offset="0%" stop-color="var(--mist-top)"/>
      <stop offset="100%" stop-color="var(--mist)"/>
    </linearGradient>
  </defs>

  <!-- Sheet -->
  <rect class="sheet" x="70" y="138" width="1032" height="925" fill="var(--white)"/>

  <!-- Header band -->
  <rect class="header-band" x="70" y="138" width="1032" height="228" fill="var(--black)"/>
  <g class="header-decoration" clip-path="url(#header-clip)">
    <circle cx="909" cy="331" r="153" fill="url(#globe-tone)" role="img" aria-label="Dekorativer Kompass mit Globus"/>
  </g>

  <text class="title title-small" x="114" y="245">UNSER</text>
  <text class="title title-large" x="114" y="298">BERATUNGS-</text>
  <text class="title title-large" x="114" y="351">KONZEPT</text>

  <!-- Upper pyramid -->
  <polygon class="pyramid-upper" points="487,366 688,366 880,698 295,698" fill="url(#mist-fade)"/>
  <polygon class="pyramid-apex" points="587,191 688,366 487,366" fill="var(--gold)"/>
  <circle class="apex-emblem" cx="587" cy="285" r="38" fill="url(#emblem-tone)" role="img" aria-label="Emblem: Globus im Kompass"/>
  <text class="label-condensed label-cream" x="588" y="355" textLength="160" lengthAdjust="spacingAndGlyphs">WIR KÜMMERN UNS UM:</text>

  <rect class="audience-illustration" x="462" y="374" width="250" height="100" fill="url(#people-tone)" role="img" aria-label="Illustration: Unternehmergruppe sowie Freiberufler mit Haus und Aktentasche"/>

  <polygon class="audience-band" points="424,474 751,474 776,519 398,519" fill="var(--navy)"/>
  <text class="audience" x="496" y="501">UNTERNEHMER/IN</text>
  <text class="audience" x="674" y="501">FREIBERUFLER/IN</text>

  <!-- Offer connectors -->
  <g class="offer-connectors" fill="none" stroke="var(--white)" stroke-width="5">
    <polyline points="475,535 430,535 430,570"/>
    <polyline points="696,535 742,535 742,570"/>
    <line x1="586" y1="548" x2="586" y2="570"/>
  </g>
  <rect class="offer-label-box" x="475" y="521" width="221" height="27" fill="var(--white)"/>
  <text class="label-condensed label-ink" x="586" y="542" textLength="176" lengthAdjust="spacingAndGlyphs">DEN WOLLEN WIR ANBIETEN:</text>

  <!-- Offers -->
  <g class="offer-card">
    <circle cx="429" cy="652" r="67" fill="var(--white)"/>
    <circle cx="429" cy="652" r="60" fill="var(--gold)"/>
    <circle cx="429" cy="589" r="25" fill="var(--white)"/>
    <circle cx="429" cy="589" r="21" fill="var(--gold-light)" stroke="var(--navy)" stroke-width="3" role="img" aria-label="Symbol: Person erreicht einen Stern"/>
    <text class="offer" x="429" y="629">FINANZIELLER</text>
    <text class="offer" x="429" y="642">ERFOLG.</text>
    <text class="offer" x="429" y="663">GUTE</text>
    <text class="offer" x="429" y="676">INVESTMENT-</text>
    <text class="offer" x="429" y="689">ERFAHRUNG</text>
  </g>
  <g class="offer-card">
    <circle cx="585" cy="652" r="67" fill="var(--white)"/>
    <circle cx="585" cy="652" r="60" fill="var(--gold)"/>
    <circle cx="585" cy="589" r="25" fill="var(--white)"/>
    <circle cx="585" cy="589" r="21" fill="var(--white)" stroke="var(--navy)" stroke-width="3" role="img" aria-label="Symbol: Hand hält Euro-Münze"/>
    <text class="offer" x="585" y="638">UMFASSENDER</text>
    <text class="offer" x="585" y="651">SCHUTZ VON</text>
    <text class="offer" x="585" y="664">VERMÖGEN UND</text>
    <text class="offer" x="585" y="677">FAMILIE</text>
  </g>
  <g class="offer-card">
    <circle cx="740" cy="652" r="67" fill="var(--white)"/>
    <circle cx="740" cy="652" r="60" fill="var(--gold)"/>
    <circle cx="740" cy="589" r="25" fill="var(--white)"/>
    <circle cx="740" cy="589" r="21" fill="var(--white)" stroke="var(--navy)" stroke-width="3" role="img" aria-label="Symbol: Zahnrad mit Tacho"/>
    <text class="offer" x="740" y="629">WENIGER</text>
    <text class="offer" x="740" y="642">VERWALTUNG.</text>
    <text class="offer" x="740" y="663">MEHR ZEIT</text>
  </g>

  <!-- Lower pyramid -->
  <polygon class="pyramid-lower" points="274,730 897,730 1059,1015 113,1015" fill="var(--sand)"/>

  <g class="step-connectors" fill="none" stroke="var(--navy)" stroke-width="5">
    <polyline points="430,719 430,759 475,759"/>
    <polyline points="742,719 742,759 696,759"/>
    <line x1="586" y1="719" x2="586" y2="744"/>
  </g>
  <rect class="step-label-box" x="475" y="744" width="221" height="29" fill="var(--navy)"/>
  <text class="label-condensed label-white" x="586" y="765" textLength="202" lengthAdjust="spacingAndGlyphs">DAZU BAUEN WIR DREI SCHRITTE:</text>

  <!-- Step 1 -->
  <g class="step">
    <polygon points="294,907 444,907 475,957 447,1007 237,1007" fill="var(--black)"/>
    <polygon points="369,778 444,907 294,907" fill="var(--slate)"/>
    <text class="step-number" x="369" y="856">II</text>
    <text class="step-title" x="369" y="883">STARKES</text>
    <text class="step-title" x="369" y="899">FUNDAMENT</text>
    <text class="step-item" x="369" y="923"><tspan class="bullet">◆ </tspan>TIEFE ANALYSE IHRER IST-</text>
    <text class="step-item" x="369" y="933">SITUATION UND IHRER ZIELE</text>
    <text class="step-item" x="369" y="955"><tspan class="bullet">◆ </tspan>WISSENSVERMITTLUNG</text>
    <text class="step-item" x="369" y="977"><tspan class="bullet">◆ </tspan>ENTWICKLUNG</text>
    <text class="step-item" x="369" y="987">EINES PERSÖNLICHEN</text>
    <text class="step-item" x="369" y="998">FINANZPLANS</text>
  </g>

  <!-- Step 2 -->
  <g class="step">
    <polygon points="511,907 661,907 718,1007 453,1007" fill="var(--black)"/>
    <polygon points="586,778 661,907 511,907" fill="var(--slate)"/>
    <text class="step-number" x="586" y="856">II</text>
    <text class="step-title" x="586" y="883">NACHHALTIGE</text>
    <text class="step-title" x="586" y="899">UMSETZUNG</text>
    <text class="step-item" x="586" y="923"><tspan class="bullet">◆ </tspan>TRANSPARENTE UND</text>
    <text class="step-item" x="586" y="933">PROVISIONSFREIE VERGÜTUNG</text>
    <text class="step-item" x="586" y="955"><tspan class="bullet">◆ </tspan>BERÜCKSICHTIGUNG</text>
    <text class="step-item" x="586" y="966">STEUERLICHER ASPEKTE</text>
    <text class="step-item" x="586" y="987"><tspan class="bullet">◆ </tspan>NOBELPREISGEKRÖNTE UND</text>
    <text class="step-item" x="586" y="998">ERFOLGREICHE ANLAGESTRATEGIE</text>
  </g>

  <!-- Step 3 -->
  <g class="step">
    <polygon points="729,907 879,907 937,1007 729,1007 700,957" fill="var(--black)"/>
    <polygon points="804,778 879,907 729,907" fill="var(--slate)"/>
    <text class="step-number" x="804" y="853">III</text>
    <text class="step-title" x="804" y="869">AKTIVE</text>
    <text class="step-title" x="804" y="885">BEGLEITUNG</text>
    <text class="step-title" x="804" y="901">UND OPTIMIERUNG</text>
    <text class="step-item" x="804" y="923"><tspan class="bullet">◆ </tspan>NOTFALLPLAN</text>
    <text class="step-item" x="804" y="943"><tspan class="bullet">◆ </tspan>ZENTRALER</text>
    <text class="step-item" x="804" y="954">ANSPRECHPARTNER ZUM</text>
    <text class="step-item" x="804" y="964">THEMA FINANZEN</text>
    <text class="step-item" x="804" y="985"><tspan class="bullet">◆ </tspan>EXPERTEN-</text>
    <text class="step-item" x="804" y="995">NETZWERK</text>
  </g>

  <!-- Footer band -->
  <polygon class="footer-band" points="113,1015 1059,1015 1090,1063 84,1063" fill="var(--gold)"/>
  <text class="footer-name" x="587" y="1041">© VEMIKO VermögensManagement GmbH &amp; Co. KG</text>
</svg>
</body>
</html>
```